依頼詳細
上記ポータルサイトのWebページデザインを依頼いたします。
両企業のHPをご覧になって企業色をご理解頂き、違和感の無い雰囲気作りを希望いたします。
メインタイトルである「ハルタカグループは子育て支援を応援しています。」は固定でお願いいたします。ロゴマーク等は添付ファイルのものをご利用ください。
尚、添付ファイルはダミーデザインです。このデザインに固執しない自由な発想で結構です。
デザイン作成にあたりスマートホンでの閲覧も考慮頂きたく思います。
サイトURL
http://www.hinata-nestlu.jp
ページ数
1ページ
希望イメージ
シンプル 複雑
単色 カラフル
暗い 明るい
日常 高級
遊び心 厳粛
未来的 伝統的
女性的 男性的
希望する色
赤系、青系、水色系、黄・オレンジ系、同社はブルー・赤・黄色の三色を基本企業色としております。
納品ファイル
• イラストレーター形式 (.ai)
補足説明
子育てに関係するサイトなので、対象となる人物像は20代以降の幅広い年齢層であることをご留意いただきたく思います。
[3/4追記]
いつもお世話になります。本案件につきましてご提案をお考え頂いております方にご案内いたします。ご提案の締切日の変更ではございませんが、クライアントに対して中間報告をしたいと存じます。つきましてはご提案頂ける状態になった方はお早めにご提案頂けましたら幸いでございます。3/12・13と土日も挟みますので、3/10の状況を報告したいと考えております。もちろん3/14の締切は変更ございませんし、早くご提案頂くことでの優遇もございませんが、当方でのプレゼン作業もございますのでご理解頂けましたら幸いでございます。ご無理申し上げますが宜しくお願いいたします。
■ 選んだ理由

この度は本案件に対しまして多数のご提案を頂き誠にありがとうございました。クライアントとの協議の結果pelirund4様のご提案デザインを採用とさせていただきます。選定方法は関連企業を含む100余名の女性によるアンケートを含む審査によります。クライアントのホームページとの親和性も問題なく、女性に好感を持たれる良好なデザインであった考えます。

■ 提案者全員のお礼・コメント

殆どの応募案はどれを採用としても問題が無いほど僅差であり、よく吟味されたデザインであったと思います。残念ながら採用とならなかった応募者の方々にも心から感謝申し上げます。またの機会がございましたら何卒宜しくお願い申し上げます。

```html
<!DOCTYPE html>
<html lang="ja">
<head>
<meta charset="utf-8">
<title>子育て支援ポータルサイト | ハルタカグループ</title>
<link rel="stylesheet" href="https://fonts.googleapis.com/css2?family=M+PLUS+Rounded+1c:wght@500;800&family=Noto+Sans+JP:wght@400;700&display=swap">
<style>
  :root {
    --coral: #ec6a5e;
    --coral-dark: #d9564b;
    --page-gray: #e6e6e6;
    --card-white: #ffffff;
    --ink: #333333;
    --ink-soft: #777777;
    --more-gray: #a9a9a9;
    --footer-white: #fafafa;
  }
  * { box-sizing: border-box; margin: 0; padding: 0; }
  html, body { width: 1200px; height: 2180px; overflow: hidden; }
  body {
    background: var(--page-gray);
    font-family: "Noto Sans JP", sans-serif;
    color: var(--ink);
    position: relative;
  }
  .hero { position: absolute; left: 0; top: 0; width: 1200px; height: 660px; }
  .hero-photo {
    position: absolute; left: 0; top: 0; width: 1200px; height: 560px;
    background: linear-gradient(120deg, #f3e3d6 0%, #f7c9c0 35%, #f5ede6 60%, #e9d2c6 100%);
  }
  .hero-band { position: absolute; left: 0; top: 470px; width: 1200px; height: 190px; }
  .brand-box {
    position: absolute; right: 40px; top: 0; width: 110px; height: 60px;
    background: var(--card-white);
    display: flex; align-items: center; justify-content: center;
    font-family: "Noto Sans JP", sans-serif; font-weight: 700; font-size: 18px; color: var(--coral);
  }
  .hero-title {
    position: absolute; left: 0; top: 548px; width: 1200px; text-align: center;
    font-family: "M PLUS Rounded 1c", sans-serif; font-weight: 800;
    font-size: 64px; line-height: 1; color: #fff; letter-spacing: 4px;
  }
  .hero-sub {
    position: absolute; left: 500px; top: 622px; width: 200px; height: 30px;
    border: 2px solid #fff; border-radius: 15px;
    color: #fff; text-align: center; font-size: 17px; line-height: 26px; letter-spacing: 3px;
    font-family: "M PLUS Rounded 1c", sans-serif; font-weight: 500;
  }
  .support-heading {
    position: absolute; left: 0; top: 700px; width: 1200px; text-align: center;
    font-size: 30px; font-weight: 700; color: var(--ink); letter-spacing: 1px;
  }
  .site-grid {
    position: absolute; left: 88px; top: 762px; width: 1024px;
    display: grid; grid-template-columns: repeat(3, 320px); column-gap: 32px; row-gap: 26px;
  }
  .site-card {
    background: var(--card-white); height: 336px; padding: 10px 10px 0;
    box-shadow: 0 1px 3px rgba(0,0,0,0.15);
    display: flex; flex-direction: column;
  }
  .site-shot { height: 168px; background: linear-gradient(160deg, #eaf6df 0%, #fdf0e4 50%, #e7f1fb 100%); }
  .site-shot.warm { background: linear-gradient(160deg, #fff4c9 0%, #e6f4d7 55%, #fbe3d9 100%); }
  .site-shot.rose { background: linear-gradient(160deg, #fde6ec 0%, #f6f0e4 55%, #e5f0f7 100%); }
  .site-meta { display: flex; justify-content: space-between; margin-top: 12px; font-size: 15px; }
  .site-name { font-weight: 700; }
  .site-date { color: var(--coral); }
  .site-text { margin-top: 6px; font-size: 12.5px; line-height: 1.55; color: var(--ink-soft); flex: 1; }
  .site-more {
    margin: 0 -10px; height: 26px; background: var(--more-gray); color: #fff;
    text-align: center; font-size: 13px; line-height: 26px; letter-spacing: 1px;
  }
  .to-top {
    position: absolute; right: 88px; top: 1842px; width: 140px; height: 28px;
    background: #d0d0d0; color: #fff; font-size: 13px; text-align: center; line-height: 28px;
  }
  .group-links {
    position: absolute; left: 0; top: 1868px; width: 1200px; height: 72px;
    display: flex; justify-content: center; gap: 16px; align-items: center;
  }
  .group-link {
    width: 230px; height: 50px; background: var(--card-white); border: 1px solid #ccc;
    display: flex; align-items: center; justify-content: center; gap: 8px;
    font-weight: 700; font-size: 16px; color: var(--ink);
  }
  .group-link .mark { width: 14px; height: 14px; background: var(--coral); }
  .policy-bar {
    position: absolute; left: 0; top: 1940px; width: 1200px; height: 40px;
    background: var(--coral); color: #fff; font-size: 14px;
    display: flex; justify-content: center; align-items: center; gap: 30px;
  }
  .site-footer {
    position: absolute; left: 0; top: 1980px; width: 1200px; height: 200px;
    background: var(--footer-white); padding: 24px 60px; font-size: 12.5px; line-height: 1.8; color: var(--ink-soft);
  }
</style>
</head>
<body>
  <header class="hero">
    <div class="hero-photo" role="img" aria-label="赤ちゃんや子どもと母親の笑顔の写真コラージュ"></div>
    <svg class="hero-band" viewBox="0 0 1200 190" preserveAspectRatio="none" aria-hidden="true">
      <path d="M0 70 Q600 -30 1200 70 L1200 190 L0 190 Z" fill="#ec6a5e"/>
      <path d="M0 70 Q600 -30 1200 70" fill="none" stroke="#ffffff" stroke-width="4"/>
    </svg>
    <div class="brand-box">ハルタカ</div>
    <h1 class="hero-title">子育て支援</h1>
    <p class="hero-sub">ポータルサイト</p>
  </header>

  <main>
    <h2 class="support-heading">＼ ハルタカグループは「子育て支援」を応援しています。／</h2>
    <section class="site-grid">
      <article class="site-card"><div class="site-shot" role="img" aria-label="子育てサイトの画面"></div><div class="site-meta"><span class="site-name">子育てサイト</span><span class="site-date">2016.03.10</span></div><p class="site-text">こちらには各サイトの紹介文が入ります。子育てに役立つ情報やイベントのお知らせを分かりやすくまとめています。</p><div class="site-more">MORE</div></article>
      <article class="site-card"><div class="site-shot warm" role="img" aria-label="子育てサイトの画面"></div><div class="site-meta"><span class="site-name">子育てサイト</span><span class="site-date">2016.03.10</span></div><p class="site-text">こちらには各サイトの紹介文が入ります。子育てに役立つ情報やイベントのお知らせを分かりやすくまとめています。</p><div class="site-more">MORE</div></article>
      <article class="site-card"><div class="site-shot rose" role="img" aria-label="子育てサイトの画面"></div><div class="site-meta"><span class="site-name">子育てサイト</span><span class="site-date">2016.03.10</span></div><p class="site-text">こちらには各サイトの紹介文が入ります。子育てに役立つ情報やイベントのお知らせを分かりやすくまとめています。</p><div class="site-more">MORE</div></article>
      <article class="site-card"><div class="site-shot" role="img" aria-label="子育てサイトの画面"></div><div class="site-meta"><span class="site-name">子育てサイト</span><span class="site-date">2016.03.10</span></div><p class="site-text">こちらには各サイトの紹介文が入ります。子育てに役立つ情報やイベントのお知らせを分かりやすくまとめています。</p><div class="site-more">MORE</div></article>
      <article class="site-card"><div class="site-shot warm" role="img" aria-label="子育てサイトの画面"></div><div class="site-meta"><span class="site-name">子育てサイト</span><span class="site-date">2016.03.10</span></div><p class="site-text">こちらには各サイトの紹介文が入ります。子育てに役立つ情報やイベントのお知らせを分かりやすくまとめています。</p><div class="site-more">MORE</div></article>
      <article class="site-card"><div class="site-shot rose" role="img" aria-label="子育てサイトの画面"></div><div class="site-meta"><span class="site-name">子育てサイト</span><span class="site-date">2016.03.10</span></div><p class="site-text">こちらには各サイトの紹介文が入ります。子育てに役立つ情報やイベントのお知らせを分かりやすくまとめています。</p><div class="site-more">MORE</div></article>
      <article class="site-card"><div class="site-shot" role="img" aria-label="子育てサイトの画面"></div><div class="site-meta"><span class="site-name">子育てサイト</span><span class="site-date">2016.03.10</span></div><p class="site-text">こちらには各サイトの紹介文が入ります。子育てに役立つ情報やイベントのお知らせを分かりやすくまとめています。</p><div class="site-more">MORE</div></article>
      <article class="site-card"><div class="site-shot warm" role="img" aria-label="子育てサイトの画面"></div><div class="site-meta"><span class="site-name">子育てサイト</span><span class="site-date">2016.03.10</span></div><p class="site-text">こちらには各サイトの紹介文が入ります。子育てに役立つ情報やイベントのお知らせを分かりやすくまとめています。</p><div class="site-more">MORE</div></article>
      <article class="site-card"><div class="site-shot rose" role="img" aria-label="子育てサイトの画面"></div><div class="site-meta"><span class="site-name">子育てサイト</span><span class="site-date">2016.03.10</span></div><p class="site-text">こちらには各サイトの紹介文が入ります。子育てに役立つ情報やイベントのお知らせを分かりやすくまとめています。</p><div class="site-more">MORE</div></article>
    </section>
    <div class="to-top">ページの先頭へ</div>
  </main>

  <nav class="group-links">
    <div class="group-link"><span class="mark"></span>ハルタカホールディングス</div>
    <div class="group-link"><span class="mark"></span>ハルタカ運輸</div>
  </nav>
  <nav class="policy-bar">
    <span>プライバシーポリシー</span><span>リンクポリシー</span><span>免責事項</span>
  </nav>
  <footer class="site-footer">
    運営機関：子育て支援 広報　〒000-0000 東京都みなと区ひなた町1-2-3　電話：000-000-0000　E-mail：info@hinata-nestlu.jp<br>
    Copyright © 2016 hinata-nestlu.jp All rights reserved.
  </footer>
</body>
</html>
```